Clinique VeraNova business card

I am looking for a talented designer who can an existing design and make it better. I need a 2 sided business card to represent our Psychology clinic staff members. It would need to be elegant, yet modern, clean, light and uplifting. Simple design, quick turnaround time. Lots of files and logos to use as your guide. I hope to hear from you!

Target Market(s)

Clients who receive the card of our therapists

Industry/Entity Type

Health And Wellness

Contact Information for Business Card

Following the similar designs of the Maplebrook Care Center card, there will be 2 sides. Side 1 (front) should have the veranova logo instead of the maplebrook care logo, The title should read Clinique VeraNova instead of centre Bien-Être Mésange/Maplebrook care Center.

Side 2 should have a spiral similar to the one on the card with sunflower leaves, and the title of the Therapist should be Marielle Odile Brunet, Psychologue, Psychologist, her email: Marielle@Veranova-example.com and phone number should be (514) 555-0137

Font styles to use
Serif

Colors
fee18a
85cae6
ffffff
0255a3

Requirements
Must have
• Side 1 (front): veranova logo- Name of the clinic, clinic address, contact info of clinic etc. use little icons in front of each (just like on sample card)
side 2: Therapist name titles and their contact info underneath with design of spiral and/or sunflower leaves..
Nice to have
• soft colors along soft yellow/gold and blue like the logo,
mini icons for phone, email, address etc.
We do work with a holistic, zen approach so it should represent that to some extent

```html
<!DOCTYPE html>
<html lang="fr">
<head>
<meta charset="utf-8">
<title>Clinique VeraNova – cartes professionnelles</title>
<link href="https://fonts.googleapis.com/css2?family=Cormorant+Garamond:wght@500;600&family=Cormorant+SC:wght@600&display=swap" rel="stylesheet">
<style>
  :root{
    --backdrop:#d4cfbc;
    --paper:#fafaf8;
    --navy:#2a2370;
    --gold:#c9b063;
    --sun:#f2dc2a;
    --sun-soft:#f8ec9a;
  }
  *{margin:0;padding:0;box-sizing:border-box}
  html,body{width:1200px;height:1200px;overflow:hidden;background:var(--backdrop)}
  body{position:relative;font-family:"Cormorant Garamond",Georgia,serif;color:var(--navy)}
  .card{position:absolute;top:287px;width:356px;height:622px;background:var(--paper);overflow:hidden}
  .card--front{left:170px}
  .card--back{left:677px}

  .brand-mark{position:absolute;top:128px;left:0;width:100%;display:flex;justify-content:center;align-items:center;gap:12px}
  .brand-mark__dot{width:22px;height:22px;border-radius:50%;background:var(--sun)}
  .brand-mark__name{font-size:54px;font-weight:500;color:var(--navy);letter-spacing:1px}

  .clinic-title{position:absolute;top:314px;width:100%;text-align:center;font-family:"Cormorant SC","Cormorant Garamond",serif;font-weight:600;font-size:27px;letter-spacing:1.5px;color:var(--gold)}

  .divider{position:absolute;left:47px;width:261px;height:14px}
  .divider::before,.divider::after{content:"";position:absolute;top:7px;width:114px;border-top:1px solid var(--gold)}
  .divider::before{left:0}
  .divider::after{right:0}
  .divider svg{position:absolute;left:123px;top:0;width:14px;height:14px;fill:var(--gold)}

  .contact-line{position:absolute;width:100%;text-align:center;font-size:17px;line-height:18px;font-weight:500}
  .contact-line--phone{letter-spacing:3px;font-size:16px}

  .therapist-name{position:absolute;top:28px;left:32px;font-size:24px;font-weight:600;color:var(--gold);display:flex;align-items:center;white-space:nowrap}
  .therapist-name::after{content:"";display:block;width:115px;margin-left:10px;border-top:1px solid var(--gold)}
  .therapist-role{position:absolute;top:56px;left:31px;font-size:16px;font-weight:500}
  .therapist-contact{position:absolute;left:31px;display:flex;align-items:center;gap:8px;font-size:17px;font-weight:500}
  .therapist-contact svg{width:14px;height:14px;fill:var(--gold)}
  .therapist-contact--phone{top:96px;letter-spacing:1.5px}
  .therapist-contact--mail{top:122px}

  .spiral-area{position:absolute;left:-60px;top:185px;width:390px;height:380px;border-radius:50%;
    background:radial-gradient(circle at 55% 55%, var(--paper) 0 18%, var(--sun-soft) 30%, rgba(248,236,154,.7) 48%, var(--sun) 62%, rgba(242,220,42,0) 72%)}
</style>
</head>
<body>
  <section class="card card--front" aria-label="Recto">
    <div class="brand-mark">
      <span class="brand-mark__dot"></span>
      <span class="brand-mark__name">VeraNova</span>
    </div>

    <h1 class="clinic-title">Clinique VeraNova</h1>

    <div class="divider" style="top:362px"><svg viewBox="0 0 24 24"><path d="M6.6 10.8a15.1 15.1 0 0 0 6.6 6.6l2.2-2.2c.3-.3.7-.4 1-.2 1.1.4 2.3.6 3.6.6.6 0 1 .4 1 1V20c0 .6-.4 1-1 1A17 17 0 0 1 3 4c0-.6.4-1 1-1h3.5c.6 0 1 .4 1 1 0 1.3.2 2.5.6 3.6.1.3 0 .7-.2 1z"/></svg></div>
    <p class="contact-line contact-line--phone" style="top:380px">514-555-0137</p>

    <div class="divider" style="top:403px"><svg viewBox="0 0 24 24"><path d="M12 2a7 7 0 0 0-7 7c0 5.2 7 13 7 13s7-7.8 7-13a7 7 0 0 0-7-7zm0 9.5A2.5 2.5 0 1 1 12 6.5a2.5 2.5 0 0 1 0 5z"/></svg></div>
    <p class="contact-line" style="top:424px">4810 boul. des Érables ouest<br>Lachine, Qc., H9R 2K4</p>

    <div class="divider" style="top:464px"><svg viewBox="0 0 24 24"><path d="M2 5h20v14H2zm2 2v.5l8 5 8-5V7z"/></svg></div>
    <p class="contact-line" style="top:482px">info@veranova-example.com</p>

    <div class="divider" style="top:508px"><svg viewBox="0 0 24 24"><path d="M12 2a10 10 0 1 0 0 20 10 10 0 0 0 0-20zm0 2c.9 0 2.2 2 2.7 5H9.3C9.8 6 11.1 4 12 4zM4.3 10.5h3.1a17 17 0 0 0 0 3H4.3a8 8 0 0 1 0-3zm5 3a15 15 0 0 1 0-3h5.4a15 15 0 0 1 0 3zm7.3 0a17 17 0 0 0 0-3h3.1a8 8 0 0 1 0 3zM12 20c-.9 0-2.2-2-2.7-5h5.4c-.5 3-1.8 5-2.7 5z"/></svg></div>
    <p class="contact-line" style="top:524px">www.veranova-example.com</p>

    <div class="divider" style="top:550px"><svg viewBox="0 0 24 24"><circle cx="12" cy="12" r="10"/></svg></div>
    <p class="contact-line" style="top:570px">www.social-example.com/VeraNova</p>
  </section>

  <section class="card card--back" aria-label="Verso">
    <h2 class="therapist-name">Marielle Odile Brunet</h2>
    <p class="therapist-role">Psychologue, Psychologist</p>
    <p class="therapist-contact therapist-contact--phone"><svg viewBox="0 0 24 24"><path d="M7 1h10a2 2 0 0 1 2 2v18a2 2 0 0 1-2 2H7a2 2 0 0 1-2-2V3a2 2 0 0 1 2-2zm0 3v15h10V4z"/></svg>(514) 555-0137</p>
    <p class="therapist-contact therapist-contact--mail"><svg viewBox="0 0 24 24"><path d="M2 5h20v14H2zm2 2v.5l8 5 8-5V7z"/></svg>Marielle@Veranova-example.com</p>
    <div class="spiral-area" role="img" aria-label="Grande spirale décorative jaune de la clinique"></div>
  </section>
</body>
</html>
```